Website Redesign - Glow Packs (2 - Pages)

We want a new website that is improved from our first website. Here is an example of a better website: http://www.gleamforte.example/
See our logo attached for design start.
Page 1:
We want a website that looks as good as this but want the following features:
- Top Bar with following Text: Whitening Kits, Whitening Pens, Pura Pulse, Pura Bristle, Accessories & Refills, Instructions, Contact Us
- Right Justified @ top My Account, Checkout
- Static top page image with our ultimate kit photo (attached: Glow Packs - Ultimate Kit.jpg) and an "Order Now" yellow button on the page (See www.velmoraharvest.example for example)
- Five Categories (Teeth Whitening Kits, Teeth Whitening Pens, Pura Pulse, Pura Bristle, Accessories & Refills) all accompanied with pictures and a text bar with name at bottom of pictures... Pura Pulse is a sonic facial brush (don't currently have picture, a filler picture is fine). Pura Bristle is an electronic tooth brush (again don't have product photo)
- Three Pictures Side by Side Pictures to explain product "Save Money", "Whiten Like a Dentist", "Fast Results" (See www.dazzlora.example under why dazz lora with three photos)...
- Reviews ("I love this product!!!", "Works great. Took only 3 sessions to a great smile", "It worked exactly as I had hoped and was simple to use")
- Bottom Order Now Bar (Again, see www.dazzlora.example bottom of page)
Page 2:
Take the instructions and make them part of a cohesive easy to follow page. See Instructions 1, 2, 3

```html
<!DOCTYPE html>
<html lang="en">
<head>
<meta charset="utf-8">
<title>Glow Packs</title>
<link rel="stylesheet" href="https://fonts.googleapis.com/css2?family=Open+Sans:wght@400;600;700&family=Arimo:wght@400;700&display=swap">
<style>
:root{
  --blue:#0d63a5;
  --blue-dark:#0a5690;
  --blue-light:#3b9be0;
  --orange-top:#f6a623;
  --orange-bottom:#d97f0c;
  --grey-band:#ececec;
  --grey-card:#f2f2f2;
  --text-grey:#666;
  --footer:#222;
  --white:#fff;
}
*{margin:0;padding:0;box-sizing:border-box}
html,body{width:821px;height:1200px;overflow:hidden;background:var(--white)}
body{position:relative;font-family:"Open Sans",Arial,sans-serif;color:#333}
.abs{position:absolute}

.account-links{top:13px;left:552px;display:flex;gap:5px}
.account-links a{display:flex;align-items:center;justify-content:center;gap:5px;height:19px;padding:0 8px;background:#e9e9e9;border-radius:2px;font-size:7.5px;letter-spacing:.5px;color:#555;text-decoration:none;text-transform:uppercase;white-space:nowrap}
.account-links a:first-child{width:74px}
.account-links a:last-child{width:78px}

.nav-bar{top:43px;left:0;width:821px;height:32px;background:var(--blue)}
.logo-badge{top:21px;left:116px;width:76px;height:76px;border-radius:50%;background:var(--blue);display:flex;align-items:center;justify-content:center;color:var(--white);font-size:11px;font-weight:600;letter-spacing:.5px;z-index:3}
.main-nav{top:43px;left:204px;height:32px;display:flex;align-items:center;gap:12px;z-index:3}
.main-nav a{color:var(--white);font-size:7.8px;letter-spacing:.7px;text-decoration:none;text-transform:uppercase;white-space:nowrap}

.hero-base{top:336px;left:0;width:821px;height:256px;background:linear-gradient(#1f77bb,var(--blue-dark))}
.hero{top:76px;left:116px;width:594px;height:292px;background:radial-gradient(ellipse at 35% 30%,#f7f8fb,#d6dbe4 75%);box-shadow:0 10px 18px rgba(0,0,0,.3);z-index:2}
.hero-frame{top:11px;left:11px;width:571px;height:269px;border:1px solid #5b8fc6}
.hero-product{top:50px;left:45px;width:310px;height:210px;border-radius:12px;background:radial-gradient(ellipse,#c9d6e8,rgba(215,222,232,0) 70%)}
.hero-title{top:77px;left:403px;color:#2a78bd;text-align:center;line-height:1}
.hero-title .t1{font-size:25px;letter-spacing:1.5px}
.hero-title .t2{font-size:20px;letter-spacing:1px;margin-top:2px;padding-bottom:6px;border-bottom:1px solid #fff}

.btn-order{display:flex;align-items:center;justify-content:center;width:152px;height:30px;border-radius:3px;background:linear-gradient(var(--orange-top),var(--orange-bottom));color:var(--white);font-size:14px;letter-spacing:1.5px;text-decoration:none;box-shadow:0 2px 3px rgba(0,0,0,.3);white-space:nowrap}
.hero .btn-order{position:absolute;top:143px;left:400px}

.section-heading{top:398px;left:127px;width:580px;display:flex;align-items:center;gap:12px;color:var(--white);font-size:16px;font-weight:400;letter-spacing:2px}
.section-heading::before,.section-heading::after{content:"";flex:1;height:4px;border-top:1px solid rgba(255,255,255,.5);border-bottom:1px solid rgba(255,255,255,.5)}

.category{top:437px;width:120px;margin-left:-60px;text-align:center}
.category .thumb{width:100px;height:100px;margin:0 auto;border-radius:50%;border:4px solid var(--blue-light);background:var(--white);display:flex;align-items:center;justify-content:center}
.category .thumb span{width:74px;height:60px;border-radius:8px;background:linear-gradient(#4fb0d6,#1b6a9e)}
.category p{margin-top:10px;color:var(--white);font-size:7.5px;font-weight:600;letter-spacing:.6px;text-transform:uppercase;white-space:nowrap}

.gap-band{top:592px;left:0;width:821px;height:10px;background:#e4e4e4}

.why-title{top:622px;left:0;width:821px;text-align:center;color:var(--blue);font-size:17px;font-weight:400;letter-spacing:1.3px}
.feature-icon{top:677px;width:128px;height:128px;margin-left:-64px;border-radius:50%;background:var(--blue);display:flex;align-items:center;justify-content:center}
.feature-icon .art{width:72px;height:64px;border-radius:20px;background:#e8eef5}
.divider{top:687px;width:1px;height:222px;background:#9fc3e2}
.divider svg{position:absolute;top:89px;left:0}
.feature-card{top:814px;width:142px;height:95px;background:var(--grey-card);border-bottom:3px solid #d0d0d0;padding:8px 8px 0;text-align:center}
.feature-card h3{color:var(--blue);font-size:10px;font-weight:600;letter-spacing:.5px;text-transform:uppercase;white-space:nowrap}
.feature-card p{margin-top:9px;font-family:Arimo,Arial,sans-serif;font-size:8px;line-height:1.35;color:var(--text-grey);text-align:justify;letter-spacing:.2px}

.reviews-band{top:931px;left:0;width:821px;height:145px;background:var(--grey-band)}
.quote-mark{font-family:Georgia,serif;font-size:130px;line-height:1;color:#d9d9d9}
.review-card{top:966px;width:197px;height:82px;background:var(--white);border-bottom:3px solid #cfcfcf}
.review-card .photo{position:absolute;top:11px;left:8px;width:60px;height:52px;border:1px solid #ccc;background:linear-gradient(#bfe0f2,#d9c1ad)}
.review-card blockquote{position:absolute;top:11px;left:73px;width:112px;font-family:Arimo,Arial,sans-serif;font-size:8.3px;line-height:1.35;color:var(--text-grey);letter-spacing:.2px;text-align:justify}
.review-card cite{position:absolute;top:52px;left:75px;font-family:Arimo,Arial,sans-serif;font-style:normal;font-size:9px;font-weight:700;color:var(--blue)}

.cta-band{top:1076px;left:0;width:821px;height:102px;background:var(--blue);display:flex;align-items:center;justify-content:center;gap:14px}
.cta-band h2{color:var(--white);font-size:22px;font-weight:400;letter-spacing:2px;text-transform:uppercase;white-space:nowrap}
.cta-band .brand{text-transform:none}

.site-footer{top:1178px;left:0;width:821px;height:22px;background:var(--footer);color:#ddd;font-size:8.5px;letter-spacing:.4px;padding-left:121px;line-height:22px}
</style>
</head>
<body>

<nav class="account-links abs">
  <a href="#"><svg width="7" height="8" viewBox="0 0 7 8"><circle cx="3.5" cy="2" r="2" fill="#555"/><path d="M0 8c0-3 7-3 7 0z" fill="#555"/></svg>My Account</a>
  <a href="#"><svg width="10" height="8" viewBox="0 0 10 8"><path d="M0 1h2l1.5 4.5h5L10 2H2.6" fill="none" stroke="#555"/><circle cx="4" cy="7" r=".9" fill="#555"/><circle cx="8" cy="7" r=".9" fill="#555"/></svg>Checkout</a>
</nav>

<div class="nav-bar abs"></div>
<div class="logo-badge abs">Glow Packs</div>
<nav class="main-nav abs">
  <a href="#">Whitening Kits</a>
  <a href="#">Whitening Pens</a>
  <a href="#">Pura Pulse</a>
  <a href="#">Pura Bristle</a>
  <a href="#">Accessories &amp; Refills</a>
  <a href="#">Instructions</a>
  <a href="#">Contact</a>
</nav>

<div class="hero-base abs"></div>
<section class="hero abs">
  <div class="hero-frame abs"></div>
  <div class="hero-product abs" role="img" aria-label="Glow Packs Ultimate Kit product photo: light, trays, gel syringe and shade guide"></div>
  <div class="hero-title abs">
    <div class="t1">GLOW PACKS</div>
    <div class="t2">ULTIMATE KIT</div>
  </div>
  <a class="btn-order" href="#">ORDER NOW</a>
</section>

<h2 class="section-heading abs">GLOW PACKS</h2>

<div class="category abs" style="left:177px"><div class="thumb"><span role="img" aria-label="Teeth whitening kit photo"></span></div><p>Teeth Whitening Kits</p></div>
<div class="category abs" style="left:298px"><div class="thumb"><span role="img" aria-label="Teeth whitening pens photo"></span></div><p>Teeth Whitening Pens</p></div>
<div class="category abs" style="left:418px"><div class="thumb"><span role="img" aria-label="Pura Pulse product photo"></span></div><p>Pura Pulse</p></div>
<div class="category abs" style="left:539px"><div class="thumb"><span role="img" aria-label="Pura Bristle product photo"></span></div><p>Pura Bristle</p></div>
<div class="category abs" style="left:660px"><div class="thumb"><span role="img" aria-label="Accessories and refills photo"></span></div><p>Accessories &amp; Refills</p></div>

<div class="gap-band abs"></div>

<h2 class="why-title abs">WHY CHOOSE GLOW PACKS</h2>

<div class="feature-icon abs" style="left:219px"><div class="art" role="img" aria-label="Piggy bank illustration"></div></div>
<div class="divider abs" style="left:320px"><svg width="8" height="16" viewBox="0 0 8 16"><path d="M0 0l7 8-7 8" fill="none" stroke="#9fc3e2"/></svg></div>
<div class="feature-icon abs" style="left:427px"><div class="art" role="img" aria-label="Cartoon tooth giving a thumbs up"></div></div>
<div class="divider abs" style="left:537px"><svg width="8" height="16" viewBox="0 0 8 16"><path d="M0 0l7 8-7 8" fill="none" stroke="#9fc3e2"/></svg></div>
<div class="feature-icon abs" style="left:635px">
  <svg width="66" height="66" viewBox="0 0 66 66"><circle cx="33" cy="33" r="30" fill="none" stroke="#fff" stroke-width="4"/><circle cx="33" cy="33" r="24" fill="none" stroke="#fff" stroke-width="1.5"/><g fill="#fff"><circle cx="33" cy="13" r="2"/><circle cx="53" cy="33" r="2"/><circle cx="33" cy="53" r="2"/><circle cx="13" cy="33" r="2"/></g><path d="M33 33V18M33 33l10 8" stroke="#fff" stroke-width="3" stroke-linecap="round"/></svg>
</div>

<article class="feature-card abs" style="left:152px"><h3>Save Money</h3><p>Lorem ipsum dolor sit amet, consectetur adipiscing elit. Sus-pendisse sed pulvinar purus. Nullam non congue augue</p></article>
<article class="feature-card abs" style="left:357px"><h3>Whiten Like a Dentist</h3><p>Lorem ipsum dolor sit amet, consectetur adipiscing elit. Sus-pendisse sed pulvinar purus. Nullam non congue augue</p></article>
<article class="feature-card abs" style="left:570px"><h3>Fast Results</h3><p>Lorem ipsum dolor sit amet, consectetur adipiscing elit. Sus-pendisse sed pulvinar purus. Nullam non congue augue</p></article>

<section class="reviews-band abs">
  <span class="quote-mark abs" style="top:-10px;left:60px">“</span>
  <span class="quote-mark abs" style="top:20px;left:732px">”</span>
</section>
<article class="review-card abs" style="left:113px"><div class="photo" role="img" aria-label="Customer portrait photo"></div><blockquote>I love this product, It really works great and you can see fast results!</blockquote><cite>-Jane Doe</cite></article>
<article class="review-card abs" style="left:327px"><div class="photo" role="img" aria-label="Customer portrait photo"></div><blockquote>I love this product, It really works great and you can see fast results!</blockquote><cite>-Jane Doe</cite></article>
<article class="review-card abs" style="left:546px"><div class="photo" role="img" aria-label="Customer portrait photo"></div><blockquote>I love this product, It really works great and you can see fast results!</blockquote><cite>-Jane Doe</cite></article>

<section class="cta-band abs">
  <h2>Get your <span class="brand">Glow Packs</span> today!</h2>
  <a class="btn-order" href="#">ORDER NOW</a>
</section>

<footer class="site-footer abs">Copyright 2014 Glow Packs.&nbsp; Terms &amp; Conditions&nbsp; |&nbsp; Privacy Policy</footer>

</body>
</html>
```